Yacht Charter Broker needs a magazine page design

We are a travel agent for yachts called Velmoria Yacht Charters. www.velmoriacharters.example We are advertising in a magazine at the grand pacer equine fair - https://plgequinefair.example/ - and need a high-end luxury feeling magazine page.

Target Market(s)

Vacation goers looking to charter a crewed yacht.

Industry/Entity Type

Travel Agent

Requirements
Must have
• luxury feel. logo. website and social media icons if you feel necessary. Our motto is: Inhale. Exhale. Sail.
• Catamaran picture, snorkeling and other island, water looking pictures.
Nice to have
• Open to your design.
Should not have
• Nothing comes to mind.

```html
<!DOCTYPE html>
<html lang="en">
<head>
<meta charset="utf-8">
<title>Velmoria Yacht Charters – Magazine Page</title>
<link rel="stylesheet" href="https://fonts.googleapis.com/css2?family=Cinzel:wght@400&family=Montserrat:wght@300;400;600;700&display=swap">
<style>
  :root {
    --backdrop: #e9e9e7;
    --panel: #17181a;
    --ink: #f2f2f2;
    --ink-soft: #c9c9c9;
    --accent: #1b84b0;
    --sea-deep: #0e4a82;
    --sea-mid: #1672a6;
    --sea-shallow: #1f97a8;
    --shore-rock: #8b8f84;
    --shore-green: #6d7a36;
    --sans: "Montserrat", Arial, sans-serif;
    --serif: "Cinzel", Georgia, serif;
  }
  * { box-sizing: border-box; margin: 0; padding: 0; }
  html, body { width: 1200px; height: 627px; overflow: hidden; }
  body { background: var(--backdrop); position: relative; font-family: var(--sans); }

  .magazine-page {
    position: absolute; left: 362px; top: 9px;
    width: 476px; height: 609px;
    display: flex;
    box-shadow: 0 6px 18px rgba(0,0,0,.25);
  }
  .info-column {
    position: relative;
    width: 235px; height: 100%;
    background: var(--panel);
    color: var(--ink);
  }
  .hero-photo {
    flex: 1;
    background: linear-gradient(180deg,
      var(--sea-deep) 0%, var(--sea-mid) 35%, var(--sea-shallow) 62%,
      #2a8f97 74%, var(--shore-rock) 84%, var(--shore-green) 100%);
  }

  .brand { position: absolute; top: 40px; left: 0; width: 100%; text-align: center; }
  .brand-name {
    font-family: var(--serif); font-weight: 400;
    font-size: 25px; letter-spacing: 3px; color: var(--ink);
  }
  .brand-tagline {
    font-family: var(--serif); font-size: 7.5px; letter-spacing: 1.2px;
    color: var(--ink-soft); margin-top: 2px; text-transform: uppercase;
  }

  .motto-frame {
    position: absolute; left: 24px; top: 109px;
    width: 211px; height: 183px;
    border: 1px solid rgba(255,255,255,.75); border-right: none;
    padding: 20px 0 0 20px;
  }
  .motto-line {
    display: block; font-weight: 300; font-size: 40px;
    line-height: 46px; color: var(--ink);
  }
  .motto-sail {
    display: block; font-weight: 700; font-size: 58px;
    line-height: 58px; color: var(--accent); letter-spacing: 1px;
  }

  .lower-content {
    position: absolute; left: 24px; right: 14px; top: 314px; bottom: 20px;
    display: flex; flex-direction: column;
  }
  .claim {
    font-size: 16px; line-height: 18px; font-weight: 400;
    text-transform: uppercase; color: var(--ink);
  }
  .claim strong { font-weight: 700; }

  .body-copy {
    margin-top: 16px;
    font-size: 6.3px; line-height: 10.4px; letter-spacing: -0.05px;
    color: var(--ink-soft);
    text-align: justify; hyphens: auto;
  }

  .contact { margin-top: auto; padding-top: 6px; }
  .website {
    font-size: 10.5px; color: var(--ink); letter-spacing: .2px;
  }
  .follow {
    margin-top: 5px;
    display: flex; align-items: center; gap: 6px;
    font-size: 9.5px; color: var(--ink);
  }
  .follow-label { margin-right: 4px; }
  .social-dot {
    width: 17px; height: 17px; border-radius: 50%;
    border: 1px solid var(--ink);
  }
</style>
</head>
<body>
  <main class="magazine-page">
    <section class="info-column">
      <header class="brand">
        <div class="brand-name">VELMORIA</div>
        <div class="brand-tagline">Yacht Charter Broker</div>
      </header>

      <div class="motto-frame">
        <span class="motto-line">INHALE,</span>
        <span class="motto-line">EXHALE,</span>
        <span class="motto-sail">SAIL</span>
      </div>

      <div class="lower-content">
        <h2 class="claim">Velmoria is<br>the <strong>world's<br>foremost in<br>yacht chartering.</strong></h2>

        <p class="body-copy">Celebrities and the super rich have long used yachts as a way of combining luxury and privacy, and a growing market has seen it become not only popular, but accessible, for those looking to experience groundbreaking travel. Forget about the tight schedule of a cruise ship and dealing with multiple reservations of hotels and restaurants - Velmoria Yacht Charters offers an adventure like no other, with freedom AND flexibility. Custom-tailored to the exact vacation you and your guests want to experience, we also put together a professional crew dedicated to perfecting your experience. Luxury accomodations, relaxation like you've never felt, breathtaking views, gourmet cuisine and endless activities. Inhale, Exhale, Sail - with Velmoria Yacht Charters.</p>

        <div class="contact">
          <div class="website">www.velmoriacharters.example</div>
          <div class="follow">
            <span class="follow-label">Follow us :</span>
            <span class="social-dot"></span>
            <span class="social-dot"></span>
            <span class="social-dot"></span>
            <span class="social-dot"></span>
          </div>
        </div>
      </div>
    </section>

    <div class="hero-photo" role="img" aria-label="Aerial photo of a white catamaran anchored in clear turquoise water above a rocky, green island shoreline"></div>
  </main>
</body>
</html>
```